LPS AUDITION

I need a post card design (front only) with this on it:
Leap Pulse Stride (this is the main title to be in all caps)
Auditions
Date: Thursday June 30th
6:30-8:30 PM in person
Address: 4172 Kestrel BLVD, Oakland CA 94605
video submissions turn in by Sunday July 3rd, 2022 email:LeapPulseStride22@movenote.test
Teens and Adults welcomed

SO PLEASE COME UP WITH A DESIGN THATS COLORFUL AND INVITING THX!

```html
<!DOCTYPE html>
<html lang="en">
<head>
<meta charset="utf-8">
<title>Leap Pulse Stride – Auditions Postcard</title>
<link rel="stylesheet" href="https://fonts.googleapis.com/css2?family=Montserrat:wght@400;600;700;800;900&display=swap">
<style>
  :root {
    --backdrop: #2d2b25;
    --paper: #ffffff;
    --salmon: #d36f69;
    --salmon-soft: #d9756f;
    --maroon: #7a2421;
    --pill-top: #e5573d;
    --pill-bottom: #b8281c;
    --ink: #3b2b2b;
    --photo-a: #c9d2ee;
    --photo-b: #8d8fd8;
    --photo-c: #e8c48a;
    --photo-d: #f2d6d5;
  }
  * { margin: 0; padding: 0; box-sizing: border-box; }
  html, body {
    width: 1200px; height: 956px; overflow: hidden;
    background: var(--backdrop);
    font-family: "Montserrat", Arial, sans-serif;
  }
  .postcard {
    position: absolute; left: 40px; top: 81px;
    width: 1120px; height: 793px;
    background: var(--paper);
    overflow: hidden;
  }
  .lower-band {
    position: absolute; left: 0; top: 415px; width: 100%; height: 378px;
    background: var(--salmon);
  }
  .dancers-photo {
    position: absolute; left: 507px; top: 26px; width: 613px; height: 610px;
    background:
      radial-gradient(ellipse at 70% 35%, var(--photo-b) 0%, rgba(141,143,216,0) 45%),
      radial-gradient(ellipse at 40% 55%, var(--photo-c) 0%, rgba(232,196,138,0) 40%),
      linear-gradient(160deg, var(--photo-d) 0%, var(--photo-a) 55%, rgba(211,111,105,0.6) 100%);
    border-radius: 40% 10% 30% 35%;
    opacity: 0.9;
  }
  .badge {
    position: absolute; left: 56px; top: 40px; width: 156px; height: 31px;
    border-radius: 10px;
    background: linear-gradient(var(--pill-top), var(--pill-bottom));
    border: 2px solid #8e1f15;
    color: #fff; font-weight: 700; font-size: 22px; line-height: 27px;
    text-align: center;
  }
  .schedule {
    position: absolute; left: 56px; top: 84px;
    color: var(--salmon); font-weight: 700; font-size: 23px; line-height: 33px;
  }
  .title {
    position: absolute; left: 0; top: 0; width: 1120px; height: 793px;
    font-family: "Montserrat", Arial, sans-serif; font-weight: 900;
  }
  .title .line-leap { fill: var(--maroon); }
  .title .line-pulse { fill: var(--salmon-soft); }
  .title .line-stride { fill: var(--paper); }
  .address {
    position: absolute; left: 54px; top: 632px; color: var(--ink);
  }
  .address .label { font-size: 22px; font-weight: 400; line-height: 30px; }
  .address .street { font-size: 22px; font-weight: 700; line-height: 30px; }
  .video-note {
    position: absolute; left: 54px; top: 705px;
    display: flex; align-items: center; gap: 17px; color: var(--ink);
  }
  .video-note p { font-size: 22px; line-height: 30px; font-weight: 400; }
  .video-note strong { font-weight: 700; }
  .email {
    position: absolute; left: 490px; top: 733px;
    display: flex; align-items: center; gap: 16px;
    color: var(--ink); font-size: 24px; font-weight: 600;
  }
</style>
</head>
<body>
  <main class="postcard">
    <div class="lower-band"></div>
    <div class="dancers-photo" role="img" aria-label="Photo of two street dancers leaping mid-air over a pink halftone dot backdrop"></div>

    <div class="badge">Auditions</div>
    <div class="schedule">
      <p>Date: Thursday June 30th</p>
      <p>6:30-8:30 PM in person</p>
    </div>

    <svg class="title" viewBox="0 0 1120 793" aria-label="LEAP PULSE STRIDE">
      <text class="line-leap" x="54" y="310" font-size="150" textLength="436" lengthAdjust="spacingAndGlyphs">LEAP</text>
      <text class="line-pulse" x="54" y="415" font-size="150" textLength="587" lengthAdjust="spacingAndGlyphs">PULSE</text>
      <text class="line-stride" x="54" y="606" font-size="240" textLength="1007" lengthAdjust="spacingAndGlyphs">STRIDE</text>
    </svg>

    <div class="address">
      <p class="label">Address:</p>
      <p class="street">4172 Kestrel BLVD, Oakland CA 94605</p>
    </div>

    <div class="video-note">
      <svg width="32" height="32" viewBox="0 0 32 32" aria-hidden="true">
        <rect x="0" y="0" width="32" height="32" rx="3" fill="#3b2b2b"/>
        <path d="M10 7 L25 16 L10 25 Z" fill="#e0322a"/>
      </svg>
      <p>video submissions turn in<br>by <strong>Sunday July 3rd, 2022</strong></p>
    </div>

    <div class="email">
      <svg width="36" height="24" viewBox="0 0 36 24" aria-hidden="true">
        <rect x="0" y="0" width="36" height="24" fill="#1f1717"/>
        <path d="M1 1 L18 14 L35 1 M1 23 L13 11 M35 23 L23 11" stroke="#d36f69" stroke-width="2" fill="none"/>
      </svg>
      <span>LeapPulseStride22@movenote.test</span>
    </div>
  </main>
</body>
</html>
```